Bright Tail Botanicals: Extracts for Pets

We need a brochure to help market the products. Bright Tail Botanicals makes Chinese Herbal Extracts for cats and dogs. We have three products to launch with. An allergy, calming, and pain formula. They are based on traditional Chinese Medicine Formulas that have been used for hundreds of years on humans and animals. I would like the logo (attached) and have one or two cat/dogs pictures. They can be any of the pics from my website. Each product should have a descrition of what it treats (can pull from website). The brochure can highlight its convient, effective, and a safe alternative. It has to include:

This statement has not been evaluated by the FDA.
This product is not intended to diagnose, treat, cure,
or prevent any disease. Bright Tail is not liable for any adverse effects.

I included a sample with some of the important info for the products - the desing does not have to be similar, just an example of the copy

*I would like the format to be in Illustrator, vector, so that I can change sizes if I need to without loosing any detail.

Target Market(s)

Pet Owners

Industry/Entity Type

Pet Care

Font styles to use
Other font styles liked:
• Universal (as logo)

Requirements
Must have
• Logo, Description of each products.
Nice to have
• Dog or cat picture

```html
<!DOCTYPE html>
<html lang="en">
<head>
<meta charset="utf-8">
<title>Bright Tail Botanicals – Extracts for Pets</title>
<link href="https://fonts.googleapis.com/css2?family=Montserrat:wght@800;900&family=Oswald:wght@600&family=Bitter:wght@400&display=swap" rel="stylesheet">
<style>
  :root {
    --backdrop: #5fa85f;
    --paper: #ffffff;
    --fold: #e4e4e4;
    --green-strong: #3aaa35;
    --stripe-dark: #7cc242;
    --stripe-light: #b9dc6f;
    --ink: #222222;
    --price: #3a3a3a;
    --amber-top: #7a3a20;
    --amber-bottom: #3d1a0e;
  }
  * { box-sizing: border-box; margin: 0; padding: 0; }
  html, body { width: 1200px; height: 900px; overflow: hidden; }
  body { background: var(--backdrop); position: relative; font-family: "Bitter", serif; }

  .brochure {
    position: absolute; left: 72px; top: 42px;
    width: 1056px; height: 816px;
    background: var(--paper);
    box-shadow: 0 10px 30px rgba(0,0,0,.25);
    overflow: hidden;
  }
  .stripes { position: absolute; inset: 0; width: 1056px; height: 816px; }
  .fold { position: absolute; top: 0; bottom: 0; width: 1px; background: var(--fold); }
  .fold--one { left: 352px; }
  .fold--two { left: 704px; }

  .panel { position: absolute; top: 0; width: 352px; height: 816px; }
  .panel--allergy { left: 0; }
  .panel--pain { left: 352px; }
  .panel--calming { left: 704px; }

  .bottle {
    position: absolute; width: 130px; height: 200px;
    border-radius: 40px 40px 14px 14px;
    background: linear-gradient(180deg, var(--amber-top), var(--amber-bottom));
  }
  .panel--allergy .bottle { left: 110px; top: 215px; }
  .panel--pain .bottle { left: 110px; top: 120px; }
  .panel--calming .bottle { left: 60px; top: 30px; }

  .product { position: absolute; left: 36px; right: 26px; }
  .panel--allergy .product { top: 440px; }
  .panel--pain .product { top: 350px; }
  .panel--calming .product { top: 258px; }

  .product__name {
    font-family: "Montserrat", sans-serif; font-weight: 900;
    color: var(--green-strong); font-size: 30px; line-height: .95;
    text-transform: uppercase; letter-spacing: -.5px;
  }
  .product__price {
    font-family: "Oswald", sans-serif; font-weight: 600;
    color: var(--price); font-size: 22px; margin: 4px 0 8px;
  }
  .product__text { font-size: 13px; line-height: 1.35; color: var(--ink); }

  .disclaimer {
    position: absolute; right: 30px; bottom: 28px; width: 300px;
    font-family: "Bitter", serif; font-size: 9px; line-height: 1.4;
    color: var(--ink); text-align: right;
  }
</style>
</head>
<body>
<main class="brochure">
  <svg class="stripes" viewBox="0 0 1056 816" aria-hidden="true">
    <polygon points="0,350 1056,-100 1056,-76 0,374" fill="var(--stripe-light)"/>
    <polygon points="0,400 1056,-50 1056,-26 0,424" fill="var(--stripe-light)"/>
    <polygon points="0,460 1056,10 1056,40 0,490" fill="var(--stripe-dark)"/>
  </svg>
  <div class="fold fold--one"></div>
  <div class="fold fold--two"></div>

  <section class="panel panel--allergy">
    <div class="bottle" role="img" aria-label="Amber dropper bottle of Allergy/Itch Relief extract with green label"></div>
    <div class="product">
      <h2 class="product__name">Allergy/<br>Itch Relief</h2>
      <p class="product__price">$39.00</p>
      <p class="product__text">This extract is for: itchy skin associated with allergies and/or sinusitis, red eyes, dermatitis, eczema, rash, excessive mucus. The formula has a drying effect as well anti-itching. The herbs can help the regulate the immune system and may only be needed during an immune response. When the symptoms clear, discontinue unless symptoms come back. If only dry skin and itching remain, try the Anemia Formula. To boost the immune system only, witout drying, there will be a separate extract coming soon.</p>
    </div>
  </section>

  <section class="panel panel--pain">
    <div class="bottle" role="img" aria-label="Amber dropper bottle of Pain Relief extract with blue label"></div>
    <div class="product">
      <h2 class="product__name">Pain: Anti<br>Inflammatory<br>and Analgesic</h2>
      <p class="product__price">$39.00</p>
      <p class="product__text">This extract is for chronic arthritic pain, hip dysplasia, as well as acute conditions including ACL tears, muscle\joint strain, spinal injury, or post-surgical recovery. It helps with inflammation and may reduce pain. Look for increased mobility and faster recovery. Dosage may be increased up to 50% for severe conditions.</p>
    </div>
  </section>

  <section class="panel panel--calming">
    <div class="bottle" role="img" aria-label="Amber dropper bottle of Calming extract with crimson label"></div>
    <div class="product">
      <h2 class="product__name">Calming</h2>
      <p class="product__price">$39.00</p>
      <p class="product__text">Calming is for pets who suffer from anxiety, hyperactivity, obsessive compulsive behavior, or trauma. The formula may also help reduce seizures and hypertension. The herbs help down regulate the nervous system without having the drugged effect of pharmaceuticals. Relaxed and calm is the goal. You can always lower the dose if it seems too strong, or increase up to 50% to increase the effects.</p>
    </div>
    <p class="disclaimer">These product statements have not been evaluated by the FDA.<br>These products are not intended to diagnose, treat, cure,<br>or prevent any disease. Bright Tail is not liable for any adverse effects.</p>
  </section>
</main>
</body>
</html>
```